Business Card Design Project

I require a business card with the following information on them for various different people;
name
m:
f:
e:
I have a logo already and will attached that. We are in the construction industry. I require something clean and simple but eye catching at the same time. You can use another colour with our logo if you like and you can style the logo as well if you wish. I am open.
Also it needs to be front and back design.
Industry/Entity Type
Construction
Requirements
Must have
- Logo, name, mobile, fax and email address.
Front and back design

```html
<!DOCTYPE html>
<html lang="en">
<head>
<meta charset="utf-8">
<title>Ridgeway Homes – Business Card, Front and Back</title>
<link rel="stylesheet" href="https://fonts.googleapis.com/css2?family=Source+Sans+3:wght@400;600;700&display=swap">
<style>
  :root {
    --backdrop: #a57c1f;
    --card-white: #ffffff;
    --green-light: #b6dc5c;
    --green-mid: #7fc23e;
    --green-deep: #58ad28;
    --grey-light: #8f8f8f;
    --grey-dark: #2f2f2f;
    --ink: #222222;
    --back-top: #4d4d4d;
    --back-bottom: #000000;
  }
  * { box-sizing: border-box; margin: 0; padding: 0; }
  html, body {
    width: 1200px; height: 686px; overflow: hidden;
    background: var(--backdrop);
    font-family: "Source Sans 3", "Helvetica Neue", Arial, sans-serif;
  }
  .canvas { position: relative; width: 1200px; height: 686px; }

  .card {
    position: absolute;
    width: 482px; height: 275px;
    border-radius: 26px;
    overflow: hidden;
  }

  /* Front */
  .card--front { left: 92px; top: 137px; background: var(--card-white); }
  .front-header { position: absolute; left: 0; top: 0; width: 100%; height: 63px; }
  .front-header__grey {
    position: absolute; inset: 0;
    background: linear-gradient(90deg, var(--grey-light) 48%, var(--grey-dark) 100%);
  }
  .front-header__green {
    position: absolute; inset: 0;
    background: linear-gradient(90deg, var(--green-light) 0%, var(--green-light) 19%, var(--green-deep) 52%);
    clip-path: polygon(0 0, 227px 0, 255px 31.5px, 227px 63px, 0 63px);
  }
  .holder-name {
    position: absolute; left: 300px; width: 110px; top: 0; height: 63px;
    display: flex; align-items: center; justify-content: center;
    color: #fff; font-weight: 700; font-size: 15px;
  }
  .brand {
    position: absolute; left: 0; right: 0; top: 128px;
    display: flex; align-items: center; justify-content: center; gap: 12px;
  }
  .brand__square { width: 28px; height: 28px; background: var(--green-deep); }
  .brand__name {
    font-size: 38px; font-weight: 400; color: var(--green-deep);
    line-height: 1; letter-spacing: 0.5px;
  }
  .contact {
    position: absolute; left: 0; right: 0;
    display: flex; justify-content: center; gap: 18px;
    font-size: 12.5px; color: var(--ink);
  }
  .contact--phones { top: 206px; }
  .contact--email { top: 225px; }
  .contact__item { display: flex; align-items: center; gap: 2px; }
  .contact__icon { width: 14px; height: 11px; fill: var(--green-deep); }

  /* Back */
  .card--back {
    left: 599px; top: 269px;
    background: linear-gradient(115deg, var(--back-top) 0%, #1b1b1b 55%, var(--back-bottom) 80%);
    display: flex; align-items: center; justify-content: center; gap: 16px;
  }
  .back-brand__square { width: 40px; height: 40px; background: var(--green-mid); }
  .back-brand__name {
    font-size: 44px; font-weight: 400; color: var(--green-mid); line-height: 1;
  }
</style>
</head>
<body>
<main class="canvas">

  <section class="card card--front" aria-label="Business card front">
    <div class="front-header">
      <div class="front-header__grey"></div>
      <div class="front-header__green"></div>
      <div class="holder-name">Your Name</div>
    </div>

    <div class="brand">
      <span class="brand__square"></span>
      <span class="brand__name">Ridgeway Homes</span>
    </div>

    <div class="contact contact--phones">
      <span class="contact__item">
        <svg class="contact__icon" viewBox="0 0 14 11" aria-hidden="true">
          <path d="M1 4 Q7 0 13 4 L11.5 6 L9.5 4.8 L9.5 3.6 Q7 2.8 4.5 3.6 L4.5 4.8 L2.5 6 Z"/>
        </svg>
        123-456-7890
      </span>
      <span class="contact__item">
        <svg class="contact__icon" viewBox="0 0 14 11" aria-hidden="true">
          <rect x="4" y="0" width="6" height="3"/>
          <rect x="1" y="3.5" width="12" height="5" rx="1"/>
          <rect x="3" y="8" width="8" height="3"/>
        </svg>
        123-456-7890
      </span>
    </div>
    <div class="contact contact--email">
      <span class="contact__item">
        <svg class="contact__icon" viewBox="0 0 14 11" aria-hidden="true">
          <rect x="1" y="1.5" width="12" height="8"/>
          <path d="M1 1.5 L7 6 L13 1.5" fill="none" stroke="#fff" stroke-width="1"/>
        </svg>
        name@website.com
      </span>
    </div>
  </section>

  <section class="card card--back" aria-label="Business card back">
    <span class="back-brand__square"></span>
    <span class="back-brand__name">Ridgeway Homes</span>
  </section>

</main>
</body>
</html>
```